IT Company requires design for Vinyl Print for Glazing NEW FITOUT!

Provide a design for Vinyl Glazing for 7 x 3.5 Metre Loading Bay - Was a warehouse - Conversion to corporate Office - the job is just for a design for the 7 x 3.5 metre loading bay area that will be glazed. We will be covering the Glaze with printed vinyl and we need a design for that. REFER TO GLASS FRONT SIGNAGE MOCK UP in image please.

We are a service and strategy focused IT Services business - 100% outsourced IT for our clients.

Something with more impact than the attached document - See Glass Front Signage page for the requirement.

Please feel free to give me a call

0438 215 906

Regards

Colin
Updates

HI - thanks for taking a look at the project Please see glass front signage in PDF for the best way to help us. Thanks Colin

I have just uploaded the mockups and roller door where the glazing goes in images.

Hi Everyone how is this going?? What do you need from me to assist with getting some designs??

Colin

Target Market(s)

business wanting the very best in IT advice and support

Industry/Entity Type

Business

Font styles to use
Other font styles liked:
• NeoSansPro

Requirements
Must have
• - Simple but with impact
Should not have
• too many colours or photos

```html
<!DOCTYPE html>
<html lang="en">
<head>
<meta charset="utf-8">
<title>Glazing Vinyl – Call Panel</title>
<link rel="stylesheet" href="https://fonts.googleapis.com/css2?family=Anton&display=swap">
<style>
  :root {
    --bg: #ffffff;
    --green: #6cbd5f;
    --navy: #003a5d;
  }
  html, body {
    margin: 0;
    padding: 0;
    width: 1200px;
    height: 599px;
    overflow: hidden;
    background: var(--bg);
  }
  .panel {
    position: relative;
    width: 1200px;
    height: 599px;
    font-family: "Anton", "Arial Narrow", sans-serif;
    text-align: center;
  }
  .invite {
    position: absolute;
    top: 59px;
    left: 0;
    width: 100%;
    margin: 0;
    font-size: 74px;
    line-height: 1.2;
    font-weight: 400;
    color: var(--green);
    letter-spacing: 0.5px;
    white-space: nowrap;
  }
  .phone {
    position: absolute;
    top: 168px;
    left: 0;
    width: 100%;
    margin: 0;
    font-size: 212px;
    line-height: 1.05;
    font-weight: 400;
    color: var(--navy);
    letter-spacing: -3px;
    white-space: nowrap;
  }
  .brand {
    position: absolute;
    top: 437px;
    left: 0;
    width: 100%;
    height: 115px;
    display: flex;
    justify-content: center;
    align-items: center;
    gap: 22px;
  }
  .brand-mark {
    width: 112px;
    height: 112px;
    background: var(--green);
  }
  .brand-name {
    font-size: 52px;
    line-height: 1;
    color: var(--navy);
    letter-spacing: 1px;
    white-space: nowrap;
  }
</style>
</head>
<body>
  <main class="panel">
    <p class="invite">Please feel free to give me a call</p>
    <p class="phone">0438 215 906</p>
    <div class="brand">
      <span class="brand-mark" aria-hidden="true"></span>
      <span class="brand-name">northbank systems</span>
    </div>
  </main>
</body>
</html>
```